Security Guard Company Postcard

I am looking for a postcard to be created so I can send to potential clients for sales and marketing purposes for my security guard division. NOT Investigations! I have added a photo of my logo and I am looking to have the following services included:
Permanent Security Services
Temporary Security Services
Emergency Services
Fire Watch
Alarm Response
Private Investigations
Background Checks
ALPR Camera Systems

Are just to name a few of our services. Please contact me at mdunbar@pivanco.com for any questions.
Thank you!
Marcus

Security

Security

• Any wording on Investigations

```html
<!DOCTYPE html>
<html lang="en">
<head>
<meta charset="utf-8">
<title>Pivanco Security Postcard</title>
<link rel="stylesheet" href="https://fonts.googleapis.com/css2?family=Jost:wght@400;500;600;700&family=Arimo:wght@400;700&display=swap">
<style>
  :root {
    --navy: #262a5a;
    --steel: #3f7197;
    --sky: #5a9cc4;
    --photo-dark: #3d3f4c;
    --photo-mid: #7c8aa0;
    --photo-light: #b9cde0;
    --paper: #ffffff;
    --backdrop: #e4e4e6;
  }
  html, body {
    margin: 0;
    padding: 0;
    width: 1200px;
    height: 802px;
    overflow: hidden;
    background: var(--backdrop);
  }
  .canvas {
    position: relative;
    width: 1200px;
    height: 802px;
  }
  .card {
    position: absolute;
    left: 309px;
    width: 572px;
    height: 357px;
    background: var(--paper);
    display: block;
  }
  .card--front { top: 25px; }
  .card--back { top: 409px; }
  .brand-name { font-family: "Jost", sans-serif; font-weight: 700; fill: var(--navy); }
  .brand-tag { font-family: "Jost", sans-serif; font-weight: 600; fill: var(--navy); letter-spacing: 2px; }
  .contact-label { font-family: "Jost", sans-serif; font-weight: 400; fill: var(--navy); letter-spacing: 2px; }
  .contact-email { font-family: "Arimo", sans-serif; font-weight: 700; fill: var(--navy); letter-spacing: 5px; }
  .contact-web { font-family: "Arimo", sans-serif; font-weight: 400; fill: var(--navy); letter-spacing: 2px; }
  .services-title { font-family: "Jost", sans-serif; font-weight: 500; fill: var(--paper); letter-spacing: 17px; }
  .service-item { font-family: "Arimo", sans-serif; font-weight: 400; fill: var(--navy); letter-spacing: 2px; }
  .service-chevron { fill: none; stroke: var(--navy); stroke-width: 3; stroke-linecap: round; stroke-linejoin: round; }
</style>
</head>
<body>
<main class="canvas">

  <svg class="card card--front" viewBox="0 0 833 520" xmlns="http://www.w3.org/2000/svg">
    <defs>
      <linearGradient id="photoTone" x1="0" y1="0" x2="1" y2="1">
        <stop offset="0" stop-color="var(--photo-mid)"/>
        <stop offset="0.35" stop-color="var(--photo-dark)"/>
        <stop offset="0.55" stop-color="var(--photo-light)"/>
        <stop offset="1" stop-color="var(--photo-mid)"/>
      </linearGradient>
      <linearGradient id="swooshTone" x1="0" y1="0" x2="1" y2="0">
        <stop offset="0" stop-color="var(--steel)"/>
        <stop offset="1" stop-color="var(--sky)"/>
      </linearGradient>
    </defs>
    <path role="img" aria-label="Close-up photograph of an eye overlaid with digital data lines"
          d="M0 0 H833 V165 C660 275 480 375 320 382 C170 388 60 360 0 308 Z"
          fill="url(#photoTone)"/>
    <path class="swoosh" d="M833 118 V168 C690 262 540 335 390 370 C560 300 700 215 833 118 Z" fill="url(#swooshTone)"/>
    <path class="swoosh" d="M0 308 C50 355 150 388 322 382 C200 410 80 410 0 372 Z" fill="url(#swooshTone)"/>

    <text class="brand-name" x="780" y="382" font-size="58" text-anchor="end">PIVANCO</text>
    <text class="brand-tag" x="780" y="409" font-size="15" text-anchor="end">SECURITY &amp; INVESTIGATIONS</text>

    <text class="contact-label" x="790" y="457" font-size="18" text-anchor="end">CONTACT  US</text>
    <text class="contact-email" x="792" y="492" font-size="24" text-anchor="end">MDUNBAR@PIVANCO.COM</text>
    <text class="contact-web" x="49" y="497" font-size="13">PIVANCO.COM</text>
  </svg>

  <svg class="card card--back" viewBox="0 0 833 520" xmlns="http://www.w3.org/2000/svg">
    <defs>
      <linearGradient id="swooshToneBack" x1="0" y1="0" x2="1" y2="0">
        <stop offset="0" stop-color="var(--steel)"/>
        <stop offset="1" stop-color="var(--sky)"/>
      </linearGradient>
    </defs>
    <path class="header-band" d="M0 0 H810 C640 120 460 225 320 242 C170 258 60 225 0 165 Z" fill="var(--navy)"/>
    <path class="swoosh" d="M810 0 H833 V18 C700 100 560 175 430 218 C580 150 700 80 810 0 Z" fill="url(#swooshToneBack)"/>
    <path class="swoosh" d="M0 182 C50 230 150 262 322 253 C200 285 80 285 0 245 Z" fill="url(#swooshToneBack)"/>

    <circle class="services-mark" cx="99" cy="153" r="27" fill="none" stroke="var(--paper)" stroke-width="4"/>
    <text class="services-title" x="153" y="172" font-size="48">SERVICES</text>

    <g class="service-list" font-size="17">
      <path class="service-chevron" d="M80 290 l6 6 l-6 6"/>
      <text class="service-item" x="127" y="303">PERMANENT SECURITY SERVICES</text>
      <path class="service-chevron" d="M80 317 l6 6 l-6 6"/>
      <text class="service-item" x="127" y="330">TEMPORARY SECURITY SERVICES</text>
      <path class="service-chevron" d="M80 343 l6 6 l-6 6"/>
      <text class="service-item" x="127" y="356">EMERGENCY SERVICES</text>
      <path class="service-chevron" d="M80 369 l6 6 l-6 6"/>
      <text class="service-item" x="127" y="382">FIRE WATCH</text>
      <path class="service-chevron" d="M80 395 l6 6 l-6 6"/>
      <text class="service-item" x="127" y="409">ALARM RESPONSE</text>
      <path class="service-chevron" d="M80 422 l6 6 l-6 6"/>
      <text class="service-item" x="127" y="435">PRIVATE INVESTIGATIONS</text>
      <path class="service-chevron" d="M80 448 l6 6 l-6 6"/>
      <text class="service-item" x="127" y="461">BACKGROUND CHECKS</text>
      <path class="service-chevron" d="M80 474 l6 6 l-6 6"/>
      <text class="service-item" x="127" y="488">ALPR CAMERA SYSTEMS</text>
    </g>

    <text class="brand-name" x="788" y="463" font-size="44" text-anchor="end">PIVANCO</text>
    <text class="brand-tag" x="788" y="481" font-size="11" text-anchor="end">SECURITY &amp; INVESTIGATIONS</text>
  </svg>

</main>
</body>
</html>
```